School District In Need of Powerful Presentation

Create a modern PPT design template -- standard and widescreen -- for the Brisco RE-8K school district inspired by its logo. The presentation should be a modern projection of 21st education that excites the people who view it. The school district is located in a rural farming community with a view of the rocky mountains to its west (check out this picture www.tentstopatmarlowbend.com/AnimatedImages/HomeGallery/000MountainScene.jpg). People in this community want quality education for their children with opportunities for them to be successful after they graduate.

Target Market(s)

The Johnstown and Milliken communities in Northern Colorado

Industry/Entity Type

Education

Font styles to use
Sans Serif

Colors
ec1f27
3176b5
acd036
fece3e
f78f20

Requirements
Must have
• The name of the school district:
• Brisco County School District RE-8K Ardenvale-Toller
• Website address: www.briscore8k.k12.zq.us/
• Email: listen@briscore8k.org
Nice to have
• A couple of color options including their current color scheme: red, gold, black
• Placeholder for pictures of students and teachers
Should not have
• Please do not use the full logo in it's current for, but you may use elements of the logo.

```html
<!DOCTYPE html>
<html lang="en">
<head>
<meta charset="utf-8">
<title>Brisco RE-8K Presentation Template</title>
<link rel="stylesheet" href="https://fonts.googleapis.com/css2?family=Arimo:wght@400;700&display=swap">
<style>
  :root {
    --sheet: #d3d3d6;
    --red: #a11c22;
    --red-dark: #7e0f14;
    --red-mid: #b3262c;
    --gold: #fdca3a;
    --gold-soft: #fff3c9;
    --gold-pale: #fffbef;
    --gold-text: #f7c531;
    --ink: #333333;
    --ink-soft: #555555;
    --black: #0d0d0d;
    --white: #ffffff;
    --rule-purple: #7a5a78;
  }
  * { box-sizing: border-box; margin: 0; padding: 0; }
  html, body { width: 1200px; height: 1062px; overflow: hidden; }
  body {
    background: var(--sheet);
    font-family: "Arimo", Arial, sans-serif;
    color: var(--ink);
    position: relative;
  }
  .slide {
    position: absolute;
    width: 563px;
    height: 316px;
    background: var(--white);
    overflow: hidden;
  }
  .col-a { left: 14px; }
  .col-b { left: 620px; }
  .row-1 { top: 14px; }
  .row-2 { top: 372px; }
  .row-3 { top: 730px; }

  /* warm title backgrounds */
  .warm-bg {
    background: linear-gradient(180deg, #fde08a 0%, #fdeaa9 45%, var(--gold-pale) 100%);
  }

  /* red brand band + footer */
  .brand-band {
    position: absolute;
    left: 0; right: 0;
    top: 210px; height: 80px;
    background: linear-gradient(90deg, #8a1117 0%, var(--red-mid) 45%, #8a1117 100%);
  }
  .brand-mark {
    position: absolute;
    top: 50%;
    transform: translateY(-50%);
    display: flex;
    align-items: center;
    gap: 10px;
  }
  .brand-mark .seal {
    width: 48px; height: 48px;
    border-radius: 50%;
    background: var(--gold-pale);
  }
  .brand-mark .name {
    font-weight: 700;
    font-size: 15px;
    color: var(--gold-text);
    letter-spacing: 0.5px;
  }
  .district-name {
    position: absolute;
    left: 310px; top: 24px;
    font-weight: 700;
    font-size: 14.5px;
    line-height: 18px;
    color: var(--gold-text);
  }
  .footer-bar {
    position: absolute;
    left: 0; right: 0;
    top: 290px; height: 26px;
    background: var(--black);
    color: var(--white);
    font-size: 9px;
    line-height: 26px;
    padding-left: 21px;
  }
  .footer-bar.centered { padding-left: 0; text-align: center; }

  /* title slide */
  .title-box {
    position: absolute;
    left: 286px; top: 110px;
    width: 277px; height: 60px;
    background: var(--gold);
    border-left: 5px solid var(--red);
    padding: 9px 0 0 16px;
  }
  .title-text {
    font-weight: 700;
    font-size: 21px;
    color: var(--red);
    line-height: 24px;
  }
  .subtitle-text {
    font-weight: 700;
    font-size: 14px;
    color: #3a3a3a;
    line-height: 17px;
  }
  .section-title {
    position: absolute;
    left: 22px; top: 106px;
  }

  /* content slides */
  .accent-tab {
    position: absolute;
    left: 0; top: 0;
    width: 5px; height: 52px;
    background: linear-gradient(180deg, var(--red) 0%, var(--red) 78%, var(--black) 78%);
  }
  .slide-heading {
    position: absolute;
    left: 22px; top: 18px;
    font-weight: 700;
    font-size: 20.5px;
    color: var(--red);
  }
  .corner-seal {
    position: absolute;
    right: 14px; top: 8px;
    width: 32px; height: 32px;
    border-radius: 50%;
    background: var(--red);
    border: 3px solid var(--gold-soft);
  }
  .heading-rule {
    position: absolute;
    left: 95px; top: 55px;
    width: 468px; height: 1px;
    background: linear-gradient(90deg, #f1d58a 0%, #e6cf9a 70%, var(--rule-purple) 100%);
  }
  .gold-base {
    position: absolute;
    left: 0; right: 0; bottom: 0;
    height: 10px;
    background: var(--gold);
  }
  .text-col {
    position: absolute;
    top: 79px;
    width: 210px;
  }
  .text-col.first { left: 21px; }
  .text-col.second { left: 288px; width: 210px; }
  .sub-heading {
    font-weight: 700;
    font-size: 8px;
    color: var(--red);
    margin-bottom: 7px;
  }
  .body-copy {
    font-size: 6.4px;
    line-height: 9.6px;
    color: var(--ink-soft);
  }
  .bullets { list-style: none; }
  .bullets li {
    position: relative;
    font-size: 6.4px;
    line-height: 9.6px;
    color: var(--ink-soft);
    padding-left: 15px;
    margin-bottom: 6px;
  }
  .bullets li::before {
    content: "";
    position: absolute;
    left: 1px; top: 3.5px;
    width: 2.5px; height: 2.5px;
    border-radius: 50%;
    background: var(--red);
  }
  .bullets.nested li { padding-left: 29px; }
  .bullets.nested li:first-child { padding-left: 15px; }
  .bullets.nested li:not(:first-child)::before { left: 15px; background: var(--ink-soft); }

  .photo-slot {
    position: absolute;
    left: 267px; top: 78px;
    width: 296px; height: 126px;
    background: linear-gradient(180deg, #b9cde3 0%, #e3e9ef 38%, #c8b58c 62%, #9d8a5c 100%);
    border-bottom: 5px solid var(--red);
  }
  .wheat-slot {
    position: absolute;
    left: 384px; top: 0;
    width: 179px; height: 245px;
    background: radial-gradient(ellipse at 55% 40%, #fdd41f 0%, #fbe27a 45%, rgba(255,255,255,0) 72%);
  }

  /* process band */
  .process-band {
    position: absolute;
    left: 0; right: 0;
    top: 200px; height: 80px;
    background: linear-gradient(180deg, #fde7a0 0%, var(--gold-pale) 100%);
  }
  .process-step {
    position: absolute;
    top: 12px;
    width: 56px; height: 56px;
    border-radius: 50%;
    background: var(--red);
    display: flex;
    align-items: center;
    justify-content: center;
  }
  .process-arrow {
    position: absolute;
    top: 34px;
    width: 0; height: 0;
    border-top: 6px solid transparent;
    border-bottom: 6px solid transparent;
    border-left: 8px solid var(--red);
  }

  .thanks {
    position: absolute;
    left: 0; right: 0; top: 112px;
    text-align: center;
    font-weight: 700;
    font-size: 64px;
    color: var(--red);
    letter-spacing: 0.5px;
  }
</style>
</head>
<body>

  <!-- Title slide -->
  <section class="slide col-a row-1 warm-bg">
    <div class="title-box">
      <div class="title-text">Your Title Goes Here</div>
      <div class="subtitle-text">Subtitle Goes Here</div>
    </div>
    <div class="brand-band">
      <div class="brand-mark" style="left:22px;">
        <span class="seal"></span>
        <span class="name">BRISCO RE-8K</span>
      </div>
      <div class="district-name">Brisco County School District<br>RE-8K Ardenvale-Toller</div>
    </div>
    <div class="footer-bar">www.briscore8k.k12.zq.us/ | listen@briscore8k.org</div>
  </section>

  <!-- Text + photo slide -->
  <section class="slide col-b row-1">
    <span class="accent-tab"></span>
    <h2 class="slide-heading">Heading Goes Here</h2>
    <span class="corner-seal"></span>
    <span class="heading-rule"></span>
    <div class="text-col first">
      <h3 class="sub-heading">Sub Heading 1</h3>
      <p class="body-copy">Use this space to share a short overview of the topic with families, staff and students. Keep each point clear and simple so the room can follow along from any seat. Add a photo of students or teachers beside the text when it helps tell the story of learning in our schools and across our growing farm community.</p>
    </div>
    <div class="photo-slot" role="img" aria-label="Photo of snow-capped mountains above open farmland"></div>
    <span class="gold-base"></span>
  </section>

  <!-- Two column slide -->
  <section class="slide col-a row-2">
    <span class="accent-tab"></span>
    <h2 class="slide-heading">Heading Goes Here</h2>
    <span class="corner-seal"></span>
    <span class="heading-rule"></span>
    <div class="text-col first">
      <h3 class="sub-heading">Sub Heading 1</h3>
      <p class="body-copy">Use this space to share a short overview of the topic with families, staff and students. Keep each point clear and simple so the room can follow along from any seat. Add a photo of students or teachers beside the text when it helps tell the story of learning in our schools and across our growing farm community.</p>
    </div>
    <div class="text-col second">
      <h3 class="sub-heading">Sub Heading 2</h3>
      <ul class="bullets">
        <li>Start with the main idea of the slide in a few words</li>
        <li>Add a supporting detail that explains why the idea matters to learners</li>
        <li>Share an example from a classroom, team or club in the district</li>
        <li>Close with a next step the audience can take after the meeting</li>
      </ul>
    </div>
    <span class="gold-base"></span>
  </section>

  <!-- Section title slide -->
  <section class="slide col-b row-2">
    <div class="wheat-slot" role="img" aria-label="Large golden wheat stalk decoration"></div>
    <div class="section-title">
      <div class="title-text">Your Title Goes Here</div>
      <div class="subtitle-text">Subtitle Goes Here</div>
    </div>
    <div class="brand-band">
      <div class="brand-mark" style="left:22px;">
        <span class="seal"></span>
        <span class="name">BRISCO RE-8K</span>
      </div>
    </div>
    <div class="footer-bar">www.briscore8k.k12.zq.us/ | listen@briscore8k.org</div>
  </section>

  <!-- Process slide -->
  <section class="slide col-a row-3">
    <span class="accent-tab"></span>
    <h2 class="slide-heading">Heading Goes Here</h2>
    <span class="corner-seal"></span>
    <span class="heading-rule"></span>
    <div class="text-col first" style="width:225px;">
      <h3 class="sub-heading">Sub-Heading 1</h3>
      <ul class="bullets">
        <li>Start with the main idea of the slide in a few words</li>
        <li>Add a supporting detail that explains why the idea matters to learners</li>
        <li>Share an example from a classroom, team or club in the district</li>
        <li>Close with a next step the audience can take after the meeting</li>
      </ul>
    </div>
    <div class="text-col second" style="width:240px;">
      <h3 class="sub-heading">Sub-Heading 2</h3>
      <ul class="bullets nested">
        <li>Start with the main idea of the slide in a few words</li>
        <li>Add a supporting detail that explains why the idea matters to learners</li>
        <li>Share an example from a classroom, team or club in the district</li>
        <li>Close with a next step the audience can take after the meeting</li>
      </ul>
    </div>
    <div class="process-band">
      <div class="process-step" style="left:136px;">
        <svg width="28" height="30" viewBox="0 0 28 30" fill="none" stroke="#fff" stroke-width="2.2" stroke-linecap="round">
          <path d="M9 19c-3-2-5-5-5-8a10 10 0 0 1 20 0c0 3-2 6-5 8v3H9z"/>
          <path d="M10 25h8M11 28h6M14 22v-7M11 13l3 2 3-2"/>
        </svg>
      </div>
      <span class="process-arrow" style="left:197px;"></span>
      <div class="process-step" style="left:214px;">
        <svg width="28" height="28" viewBox="0 0 28 28" fill="none" stroke="#fff" stroke-width="3" stroke-linecap="round">
          <path d="M22 9a10 10 0 0 0-17 3"/><path d="M6 19a10 10 0 0 0 17-3"/>
          <path d="M22 3v6h-6M6 25v-6h6"/>
        </svg>
      </div>
      <span class="process-arrow" style="left:275px;"></span>
      <div class="process-step" style="left:293px;">
        <svg width="28" height="28" viewBox="0 0 28 28" fill="none" stroke="#fff" stroke-width="3" stroke-linecap="round">
          <path d="M14 3v10"/><path d="M8 7a10 10 0 1 0 12 0"/>
        </svg>
      </div>
      <span class="process-arrow" style="left:354px;"></span>
      <div class="process-step" style="left:371px;">
        <svg width="30" height="30" viewBox="0 0 30 30" fill="#fff">
          <circle cx="11" cy="13" r="7"/><circle cx="21" cy="22" r="5"/><circle cx="22" cy="7" r="3.5"/>
          <circle cx="11" cy="13" r="2.6" fill="#a11c22"/><circle cx="21" cy="22" r="1.8" fill="#a11c22"/>
        </svg>
      </div>
    </div>
    <span class="gold-base"></span>
  </section>

  <!-- Closing slide -->
  <section class="slide col-b row-3 warm-bg">
    <div class="thanks">Thank You</div>
    <div class="brand-band">
      <div class="brand-mark" style="left:50%; transform:translate(-50%,-50%);">
        <span class="seal"></span>
        <span class="name">BRISCO RE-8K</span>
      </div>
    </div>
    <div class="footer-bar centered">www.briscore8k.k12.zq.us/ | listen@briscore8k.org</div>
  </section>

</body>
</html>
```